Website Design for Business Law Firm

We have a logo and now we would like a web site design for our new website. Our small firm provides creative and aggressive transactional (not litigation) legal services to advise healthcare, technology, internet-based and traditional companies and investors in such companies on healthcare, technology, financing, mergers/acquisitions, real estate and other transactions, legal compliance and general corporate and business matters.

We would like to see a website design that is professional and appropriate for executives, professionals, investors and government regulators to visit, that conveys professionalism and competence while being a little edgy and modern - no typical legal motifs such as gavels, books, or scales of justice. We advise businesses and investors and guide them through complicated issues quickly, capably and differently from other law firms. We are part of the business team and get things done.

The logo is attached, and we like gray as a color to complement it. The intention of the logo is to convey that in a storm or challenging time, people come to this firm, and people come to this firm when they need the power and disruption to change things or shake them up.

I have also enclosed a picture of our business card for consideration.

On the other hand, you can check out the current simple site at www.venhollow.example to see we have used a space motif in the past to evoke that we help create stars (the nebula featured there). This is not a necessary part of the new website and it may look better without it.

We appreciate your creativity and look forward to designs.

Industry/Entity Type

Business

Requirements
Must have
• We anticipate the following pages, and you may submit different ideas for the different pages:
• 1. Landing page
• 2. Services pages - healthcare, IT/Technology, general counsel services, financings, mergers/acquisitions, mediation/arbitration, procurement and productization
• 3. About Us including contact information
• Our name and contact information:
• Quellane Law Firm, P.C.
• 8716 SW 19th Ave.
• Portland, OR 97213
• phone: 971.555.0143
• fax: 971.555.0187
Nice to have
• Please consider designs that enhance the impressions we are looking for
Should not have
• Please no gavels, scales of justice, law books, or similar traditional legal imagery.

```html
<!DOCTYPE html>
<html lang="en">
<head>
<meta charset="utf-8">
<title>Quellane Law Firm</title>
<link rel="stylesheet" href="https://fonts.googleapis.com/css2?family=Maven+Pro:wght@400;500;700&family=Arimo:wght@400;700&display=swap">
<style>
:root{
  --bg-dark:#161616;
  --bg-header:#0d0d0d;
  --bg-contact:#141414;
  --bg-footer:#080808;
  --panel:#1c1c1c;
  --panel-head:#262626;
  --accent:#3f8a99;
  --text:#e6e6e6;
  --text-soft:#bdbdbd;
  --text-dim:#4e4e4e;
  --field:#050505;
  --field-line:#2e4e56;
}
*{margin:0;padding:0;box-sizing:border-box}
html,body{width:960px;height:1200px;overflow:hidden;background:var(--bg-dark)}
body{position:relative;font-family:"Arimo",Arial,sans-serif;color:var(--text)}
.abs{position:absolute}

/* header */
.site-header{left:0;top:0;width:960px;height:85px;background:var(--bg-header);border-bottom:1px solid var(--accent)}
.brand{left:160px;top:22px;display:flex;align-items:center;gap:10px}
.brand-mark{width:14px;height:14px;background:#8a9aa0}
.brand-name{font-family:"Maven Pro",sans-serif;font-weight:500;font-size:26px;letter-spacing:4px;color:#c8d2d6}
.main-nav{left:424px;top:19px;list-style:none;font-family:"Maven Pro",sans-serif;font-size:12px}
.main-nav li{height:16px;line-height:16px;padding-left:8px;width:72px}
.main-nav li.active{background:#2c2c2c}
.head-contact{font-size:10px;line-height:16px;color:var(--text)}
.head-contact b{font-size:11px}

/* hero */
.hero{left:0;top:86px;width:960px;height:252px;background:linear-gradient(90deg,#cfd6d9 0%,#eef3f5 30%,#9fc6cf 55%,#e8eef0 80%,#f4f6f7 100%)}
.hero-headline{left:449px;top:108px;font-family:"Maven Pro",sans-serif;color:#1b1b1b;line-height:32px}
.hero-headline .strong{font-weight:700;font-size:30px;letter-spacing:-1px}
.hero-headline .light{font-weight:400;font-size:25px;letter-spacing:-.5px}

/* services panel */
.services{left:551px;top:293px;width:288px;height:397px;background:var(--panel);border-radius:0 0 22px 22px;border:1px solid #2a2a2a;border-top:none}
.services-head{left:0;top:0;width:288px;height:47px;background:var(--panel-head);border-top:2px solid #3a3a3a;border-bottom:2px solid #333}
.services-head h2{position:absolute;left:48px;top:12px;font-family:"Maven Pro",sans-serif;font-size:21px;font-weight:400;color:var(--text-soft)}
.services-head h2 span{font-weight:700;color:#f2f2f2}
.service-list{position:absolute;left:24px;top:64px;list-style:none;font-size:10px}
.service-list li{height:19.2px;line-height:19.2px;display:flex;align-items:center;gap:12px}
.service-list svg{width:14px;height:10px;flex:none}

/* welcome */
.welcome{left:160px;top:380px;width:339px}
.welcome .kicker{font-family:"Maven Pro",sans-serif;font-size:24px;color:var(--text-soft);line-height:24px}
.welcome h1{font-family:"Maven Pro",sans-serif;font-weight:700;font-size:30px;line-height:32px;color:#fff}
.welcome p{font-size:9.6px;line-height:17.6px;text-align:justify;color:var(--text-soft);margin-top:20px}
.welcome p + p{margin-top:17.6px}

/* contact */
.contact-band{left:0;top:763px;width:960px;height:374px;background:var(--bg-contact);border-top:1px solid var(--accent)}
.section-title{font-family:"Maven Pro",sans-serif;font-weight:700;font-size:32px;color:#fff}
.contact-text{font-size:10px;line-height:16px;color:var(--text)}
.contact-text b{font-size:11px}
.label{font-size:9.6px;color:var(--text)}
.field{background:var(--field);border:1px solid var(--field-line);border-radius:2px}
.field .ph{position:absolute;left:38px;top:8px;font-family:"Maven Pro",sans-serif;font-size:11px;color:#777}
.field svg{position:absolute;left:10px;top:9px}
.send{left:354px;top:1058px;width:171px;height:28px;background:var(--field);color:#fff;font-size:11px;text-align:center;line-height:28px}
.map{left:556px;top:857px;width:283px;height:231px;border:2px solid #fff;background:linear-gradient(135deg,#d8d8d8,#c9c9c9)}

/* footer */
.site-footer{left:0;top:1137px;width:960px;height:63px;background:var(--bg-footer)}
.footer-brand{left:160px;top:20px;display:flex;align-items:center;gap:8px;opacity:.3}
.footer-brand .brand-mark{width:10px;height:10px}
.footer-brand .brand-name{font-size:18px;letter-spacing:3px}
.footer-nav{top:28px;font-family:"Maven Pro",sans-serif;font-size:11px;color:var(--text-dim)}
.copyright{left:721px;top:28px;font-size:10px;color:var(--text-soft)}
</style>
</head>
<body>

<header class="site-header abs">
  <div class="brand abs"><span class="brand-mark"></span><span class="brand-name">QUELLANE</span></div>
  <ul class="main-nav abs">
    <li class="active">Home</li><li>Our Service</li><li>Contact Us</li>
  </ul>
  <svg class="abs" style="left:554px;top:20px" width="30" height="44" viewBox="0 0 30 44"><path d="M8 2 L14 2 L16 12 L11 15 Q12 26 20 32 L25 28 L30 36 L25 43 Q4 38 2 10 Z" fill="#3a3a3a"/></svg>
  <div class="head-contact abs" style="left:594px;top:17px">info@quellane.example<br>Ph. <b>971 555 0143</b><br>Fax. <b>971 555 0162</b></div>
  <svg class="abs" style="left:700px;top:20px" width="36" height="46" viewBox="0 0 36 46"><path d="M18 1 A17 17 0 0 1 35 18 Q35 30 18 45 Q1 30 1 18 A17 17 0 0 1 18 1 Z" fill="#3a3a3a"/><circle cx="18" cy="18" r="6" fill="#0d0d0d"/></svg>
  <div class="head-contact abs" style="left:742px;top:17px">Quellane Law Firm, P.C.<br>8716 SW 19th Ave.<br>Portland, OR 97213</div>
</header>

<div class="hero abs" role="img" aria-label="Photo of a smiling businessman in a suit with colleagues blurred in an office behind him"></div>
<div class="hero-headline abs">
  <span class="strong">Pragmatic,</span> <span class="light">Creative Services for</span><br>
  <span class="strong">Innovative Businesses</span>
</div>

<section class="welcome abs">
  <div class="kicker">Welcome</div>
  <h1>Quellane Law Firm</h1>
  <p>Lorem ipsum dolor sit amet, consectetur adipisicing elit, sed do eiusmod tempor incididunt ut labore et dolore magna aliqua. Ut enim ad minim veniam, quis nostrud exercitation ullamco laboris nisi ut aliquip ex ea commodo consequat. Duis aute irure dolor in reprehenderit in voluptate velit esse cillum dolore eu fugiat nulla pariatur. Excepteur sint occaecat cupidatat non proident, sunt in culpa qui officia deserunt mollit anim id est laborum.</p>
  <p>Sed ut perspiciatis unde omnis iste natus error sit voluptatem accusantium doloremque laudantium, totam rem aperiam, eaque ipsa quae ab illo inventore veritatis et quasi architecto beatae vitae dicta sunt explicabo. Nemo enim ipsam voluptatem quia voluptas sit aspernatur aut odit aut fugit, sed quia consequuntur magni dolores eos qui ratione voluptatem sequi nesciunt. Neque porro quisquam est, qui dolorem ipsum quia dolor sit amet, consectetur, adipisci velit, sed quia non numquam eius modi tempora incidunt ut labore et dolore magnam aliquam quaerat voluptatem ncidunt ut labore et ncidunt ut labore et &nbsp;dolore magnam aliquam quaerat voluptatem ncidunt ut labore et ncidunt ut labore .</p>
</section>

<aside class="services abs">
  <div class="services-head abs"><h2>Our <span>Services</span></h2></div>
  <ul class="service-list">
    <li><svg viewBox="0 0 14 10"><path d="M0 0 L14 5 L0 10 L4 5 Z" fill="#6a6a6a"/></svg>Strategic Alliances</li>
    <li><svg viewBox="0 0 14 10"><path d="M0 0 L14 5 L0 10 L4 5 Z" fill="#6a6a6a"/></svg>Business Relationships</li>
    <li><svg viewBox="0 0 14 10"><path d="M0 0 L14 5 L0 10 L4 5 Z" fill="#6a6a6a"/></svg>Outsourcing</li>
    <li><svg viewBox="0 0 14 10"><path d="M0 0 L14 5 L0 10 L4 5 Z" fill="#6a6a6a"/></svg>Procurements - Buying or Selling</li>
    <li><svg viewBox="0 0 14 10"><path d="M0 0 L14 5 L0 10 L4 5 Z" fill="#6a6a6a"/></svg>Licensing and Technology Exploitation</li>
    <li><svg viewBox="0 0 14 10"><path d="M0 0 L14 5 L0 10 L4 5 Z" fill="#6a6a6a"/></svg>Venture Formation and Startup</li>
    <li><svg viewBox="0 0 14 10"><path d="M0 0 L14 5 L0 10 L4 5 Z" fill="#6a6a6a"/></svg>Venture Financing</li>
    <li><svg viewBox="0 0 14 10"><path d="M0 0 L14 5 L0 10 L4 5 Z" fill="#6a6a6a"/></svg>Creative Private Financing Arrangements</li>
    <li><svg viewBox="0 0 14 10"><path d="M0 0 L14 5 L0 10 L4 5 Z" fill="#6a6a6a"/></svg>Mergers and Acquisitions</li>
    <li><svg viewBox="0 0 14 10"><path d="M0 0 L14 5 L0 10 L4 5 Z" fill="#6a6a6a"/></svg>Real Estate</li>
    <li><svg viewBox="0 0 14 10"><path d="M0 0 L14 5 L0 10 L4 5 Z" fill="#6a6a6a"/></svg>Contracts</li>
    <li><svg viewBox="0 0 14 10"><path d="M0 0 L14 5 L0 10 L4 5 Z" fill="#6a6a6a"/></svg>Audits, Analyses and Legal Project Management</li>
    <li><svg viewBox="0 0 14 10"><path d="M0 0 L14 5 L0 10 L4 5 Z" fill="#6a6a6a"/></svg>Local Counsel for Transactions and Due Diligence</li>
    <li><svg viewBox="0 0 14 10"><path d="M0 0 L14 5 L0 10 L4 5 Z" fill="#6a6a6a"/></svg>Vendor Management</li>
    <li><svg viewBox="0 0 14 10"><path d="M0 0 L14 5 L0 10 L4 5 Z" fill="#6a6a6a"/></svg>Dispute Resolution</li>
    <li><svg viewBox="0 0 14 10"><path d="M0 0 L14 5 L0 10 L4 5 Z" fill="#6a6a6a"/></svg>Service as a Mediator or Arbitrator</li>
  </ul>
</aside>

<section class="contact-band abs">
  <h2 class="section-title abs" style="left:160px;top:42px">Contact Us</h2>
  <h2 class="section-title abs" style="left:568px;top:42px">Map</h2>

  <svg class="abs" style="left:158px;top:104px" width="30" height="46" viewBox="0 0 30 44"><path d="M8 2 L14 2 L16 12 L11 15 Q12 26 20 32 L25 28 L30 36 L25 43 Q4 38 2 10 Z" fill="#050505"/></svg>
  <div class="contact-text abs" style="left:203px;top:104px">info@quellane.example<br>Ph. <b>971 555 0143</b><br>Fax. <b>971 555 0162</b></div>
  <svg class="abs" style="left:306px;top:104px" width="36" height="46" viewBox="0 0 36 46"><path d="M18 1 A17 17 0 0 1 35 18 Q35 30 18 45 Q1 30 1 18 A17 17 0 0 1 18 1 Z" fill="#050505"/><circle cx="18" cy="18" r="6" fill="#141414"/></svg>
  <div class="contact-text abs" style="left:354px;top:104px">Quellane Law Firm, P.C.<br>8716 SW 19th Ave.<br>Portland, OR 97213</div>

  <div class="label abs" style="left:160px;top:189px">Name</div>
  <div class="field abs" style="left:160px;top:203px;width:181px;height:28px"></div>
  <div class="label abs" style="left:160px;top:237px">Email</div>
  <div class="field abs" style="left:160px;top:250px;width:181px;height:28px">
    <svg width="12" height="9" viewBox="0 0 12 9"><rect width="12" height="9" fill="#666"/><path d="M0 0 L6 5 L12 0" stroke="#050505" fill="none"/></svg>
    <span class="ph">name@domain.com</span>
  </div>
  <div class="label abs" style="left:160px;top:284px">Phone</div>
  <div class="field abs" style="left:160px;top:295px;width:181px;height:28px">
    <svg width="10" height="10" viewBox="0 0 10 10"><path d="M2 0 L4 0 L5 3 L3 4 Q4 6 6 7 L7 5 L10 6 L10 8 Q9 10 7 10 Q0 8 0 2 Q0 0 2 0 Z" fill="#666"/></svg>
    <span class="ph">555-567-1205</span>
  </div>
  <div class="label abs" style="left:354px;top:190px">Your message</div>
  <div class="field abs" style="left:354px;top:203px;width:171px;height:87px"></div>
</section>
<div class="send abs">Send</div>
<div class="map abs" role="img" aria-label="Street map of the neighbourhood around the firm's office with a location marker"></div>

<footer class="site-footer abs">
  <div class="footer-brand abs"><span class="brand-mark"></span><span class="brand-name">QUELLANE</span></div>
  <span class="footer-nav abs" style="left:400px">Home</span>
  <span class="footer-nav abs" style="left:477px">Our Service</span>
  <span class="footer-nav abs" style="left:582px">Contact Us</span>
  <span class="copyright abs">© 2013. All rights reserved.</span>
</footer>

</body>
</html>
```